FACEBOOK PAGE FOR BREVLO PLUMBING GROUP

We need a facebook banner for our new plumbing business.

Needs to be catchy and inline with our logo.

Phone: 0472 836 291
Email: hello@brevlo.com.au
website: www.brevlo.com.au
Servicing: Perth Metro Areas and surrounding suburbs
Services:
*We offer a wide range of services, including:
Plumbing – General maintenance, blocked drains, toilet repairs, burst pipes, reticulation, renovations & emergencies.

*Hot Water – Installation, servicing & repairs for all systems.

*Cooling & Heating – Air conditioning, evaporative cooling & heater servicing.

*Filtration – Filtered taps, under-sink systems & whole-house filtration setups.

Our Mission

Brevlo Group believes plumbing shouldn't break the bank - or your trust. Our mission is to provide honest, affordable, and no-nonsense plumbing services that get the job done right the first time. No runaround - just reliable work, and the respect every customer deserves.

What Makes Us Different???

Upfront Fixed Pricing
No surprises, no hidden fees. You get clear, honest quotes before any work begins.

Respectful, Customer-First Service
We show up on time, communicate clearly, and treat your property like it’s our own.

Locals Serving Locals
We’re proud to support the Perth community with reliable, high-quality plumbing backed by real local care.

FOR THE DESIGNER A little background on us as a new biz for your reference:
By Locals, For Locals
After 13 years in the plumbing industry, seasoned local plumber Wade founded his company to address the widespread issue of homeowners and businesses being overcharged or receiving inferior work. He knew there had to be a better way—and that’s when Brevlo was created.
Today, Brevlo Group is a trusted plumbing company based in Osborne Park, proudly serving residential, commercial, and industrial clients across the Perth metro area. With over a decade of experience, we deliver expert workmanship, fair pricing, and treat every job—big or small—with the same care and professionalism.
Need it done right—and affordably? Get it sorted with BREVLO now!

```html
<!DOCTYPE html>
<html lang="en">
<head>
<meta charset="utf-8">
<title>Brevlo Plumbing Group – Facebook Cover</title>
<link rel="stylesheet" href="https://fonts.googleapis.com/css2?family=Montserrat:wght@500;600;700&display=swap">
<style>
  :root {
    --navy: #2b2c6a;
    --sky: #29abe2;
    --deep-blue: #0b67a6;
    --panel-top: #cdebf9;
    --panel-bottom: #38b2ea;
    --paper: #eef2f7;
    --white: #ffffff;
  }
  * { margin: 0; padding: 0; box-sizing: border-box; }
  html, body { width: 1200px; height: 440px; overflow: hidden; background: var(--white); }
  body { font-family: "Montserrat", Arial, sans-serif; color: var(--navy); }

  .cover { position: relative; width: 1200px; height: 440px; overflow: hidden; background: var(--paper); }

  .pipe-backdrop {
    position: absolute; left: 0; top: 0; width: 835px; height: 440px;
    background: radial-gradient(ellipse at 45% 40%, #f3f6fa 0%, #e6ebf1 60%, #dde3ea 100%);
  }

  .brand-name {
    position: absolute; left: 189px; top: 84px;
    font-size: 94px; font-weight: 600; letter-spacing: 12px; line-height: 1;
    color: var(--deep-blue);
  }
  .tagline {
    position: absolute; left: 193px; top: 190px; width: 460px;
    font-size: 31px; font-weight: 600; line-height: 33px; letter-spacing: 12px;
    color: var(--navy);
  }
  .tagline span { display: block; white-space: nowrap; }
  .tagline .tight { letter-spacing: 7.2px; }

  .promises { position: absolute; left: 193px; top: 280px; list-style: none; }
  .promises li { display: flex; align-items: center; height: 32px; margin-bottom: 6.5px; }
  .tick-box {
    width: 32px; height: 32px; background: var(--sky); margin-right: 13px;
    display: flex; align-items: center; justify-content: center;
  }
  .promise-text { font-size: 28px; font-weight: 500; white-space: nowrap; }

  .service-panel {
    position: absolute; left: 835px; top: 0; width: 365px; height: 440px;
    background: linear-gradient(160deg, var(--panel-top) 0%, #7fcff2 45%, var(--panel-bottom) 100%);
  }
  .services { position: absolute; left: 38px; top: 82px; list-style: none; }
  .services li { display: flex; align-items: center; height: 36px; margin-bottom: 7.7px; }
  .service-icon { width: 28px; height: 28px; margin-right: 12px; }
  .service-name { font-size: 28px; font-weight: 700; white-space: nowrap; }

  .coverage {
    position: absolute; left: 60px; top: 309px; width: 305px; height: 71px;
    background: var(--deep-blue); border-radius: 12px 0 0 12px;
    color: var(--white); padding: 17px 0 0 14px;
  }
  .coverage-main { font-size: 19.5px; font-weight: 700; letter-spacing: 0.3px; line-height: 21px; white-space: nowrap; }
  .coverage-sub { font-size: 13.2px; font-weight: 700; letter-spacing: 0.4px; line-height: 17px; white-space: nowrap; }

  .contact {
    position: absolute; top: 416px; display: flex; align-items: center;
    font-size: 10px; font-weight: 500; color: var(--navy); white-space: nowrap; line-height: 12px;
  }
  .contact svg { width: 11px; height: 11px; margin-right: 6px; flex: none; }
  .contact-phone { left: 10px; }
  .contact-email { left: 107px; }
  .contact-web { left: 241px; }
</style>
</head>
<body>
<main class="cover">
  <div class="pipe-backdrop" role="img" aria-label="Faint photograph of chrome plumbing pipes and fittings"></div>

  <h1 class="brand-name">BREVLO</h1>
  <p class="tagline"><span>RELIABLE LOCAL</span><span class="tight">PLUMBING SERVICES</span></p>

  <ul class="promises">
    <li><span class="tick-box"><svg width="18" height="14" viewBox="0 0 18 14"><path d="M2 7l5 5 9-10" fill="none" stroke="#fff" stroke-width="2.4" stroke-linecap="round" stroke-linejoin="round"/></svg></span><span class="promise-text">Fixed Pricing No Hidden Fees</span></li>
    <li><span class="tick-box"><svg width="18" height="14" viewBox="0 0 18 14"><path d="M2 7l5 5 9-10" fill="none" stroke="#fff" stroke-width="2.4" stroke-linecap="round" stroke-linejoin="round"/></svg></span><span class="promise-text">Local &amp; Trusted</span></li>
    <li><span class="tick-box"><svg width="18" height="14" viewBox="0 0 18 14"><path d="M2 7l5 5 9-10" fill="none" stroke="#fff" stroke-width="2.4" stroke-linecap="round" stroke-linejoin="round"/></svg></span><span class="promise-text">Respectful Service</span></li>
  </ul>

  <aside class="service-panel">
    <ul class="services">
      <li>
        <svg class="service-icon" viewBox="0 0 28 28" fill="#2b2c6a"><path d="M4 4h14v4h-8v4H4z"/><circle cx="16" cy="16" r="5" fill="none" stroke="#2b2c6a" stroke-width="2.5"/><path d="M19.5 19.5l5 5" stroke="#2b2c6a" stroke-width="3" stroke-linecap="round"/><path d="M6 16c-1.5 2.5-2 3.5-2 4.5a2 2 0 004 0c0-1-.5-2-2-4.5z"/></svg>
        <span class="service-name">Plumbing</span>
      </li>
      <li>
        <svg class="service-icon" viewBox="0 0 28 28" fill="#2b2c6a"><path d="M14 2c1 5 8 8 8 15a8 8 0 01-16 0c0-4 2-6 4-8 0 3 1 4 3 5-1-5 0-9 1-12z"/></svg>
        <span class="service-name">Hot Water</span>
      </li>
      <li>
        <svg class="service-icon" viewBox="0 0 28 28" fill="none" stroke="#2b2c6a" stroke-width="2.2" stroke-linecap="round"><path d="M14 2v24M3.6 8l20.8 12M3.6 20L24.4 8M11 4l3 3 3-3M11 24l3-3 3 3"/></svg>
        <span class="service-name">Cooling &amp; Heating</span>
      </li>
      <li>
        <svg class="service-icon" viewBox="0 0 28 28" fill="#2b2c6a"><circle cx="6" cy="4" r="2"/><circle cx="14" cy="4" r="2"/><circle cx="22" cy="4" r="2"/><path d="M2 9h24l-9 9v8h-6v-8z"/></svg>
        <span class="service-name">Filtration</span>
      </li>
    </ul>

    <div class="coverage">
      <p class="coverage-main">SERVICING PERTH METRO</p>
      <p class="coverage-sub">AREAS &amp; SURROUNDING SUBURBS</p>
    </div>

    <span class="contact contact-phone"><svg viewBox="0 0 12 12" fill="#2b2c6a"><path d="M2.5 0.5l2 2.5-1 1.3c.8 1.6 2 2.8 3.6 3.6l1.3-1 2.5 2-1 2.5C5 11 1 7 .5 1.5z"/></svg>0472 836 291</span>
    <span class="contact contact-email"><svg viewBox="0 0 12 12" fill="none" stroke="#2b2c6a" stroke-width="1.5"><rect x="0.8" y="2" width="10.4" height="8"/><path d="M1 2.5l5 4 5-4"/></svg>hello@brevlo.com.au</span>
    <span class="contact contact-web"><svg viewBox="0 0 12 12" fill="none" stroke="#2b2c6a" stroke-width="1"><circle cx="6" cy="6" r="5.3"/><ellipse cx="6" cy="6" rx="2.3" ry="5.3"/><path d="M0.7 6h10.6M1.5 3.3h9M1.5 8.7h9"/></svg>www.brevlo.com.au</span>
  </aside>
</main>
</body>
</html>
```